Holiday PROMO Flyer for Healthy Restaurant

Hi ! We need a holiday style promo flyer for Verandel . Please have a holiday vibe type of design in the background. Include at least 1 of the photos that I provide, and our logo of course. This promo is for a new package that we will be offering until December 31st 2022.

It will have a promo of some type of design that says the following in a creative way:
" HOLIDAY PACKAGE PROMO!"
Buy our holiday package of $500 and receive a $100 gift card!" (THIS SHOULD BE VERY NOTICEABLE AS THIS IS THE ACTUAL PROMO)
Our biggest promo to date.
Offer ends December 31st, 2022.

Take a look at our website to stay consistant with the brand as well.

Industry/Entity Type

Restaurant

Requirements
Must have
• Logo, food photo and gift card photo

```html
<!DOCTYPE html>
<html lang="en">
<head>
<meta charset="utf-8">
<title>Verandel Holiday Package Promo</title>
<link rel="stylesheet" href="https://fonts.googleapis.com/css2?family=Londrina+Solid:wght@400;900&family=Bebas+Neue&family=Montserrat:wght@700&family=Roboto:wght@400&display=swap">
<style>
  :root {
    --backdrop: #d4d4d4;
    --paper: #ffffff;
    --band: #ececec;
    --green: #a0c035;
    --grey: #959595;
    --doodle: #e4e4e4;
  }
  * { margin: 0; padding: 0; box-sizing: border-box; }
  html, body { width: 1200px; height: 1200px; overflow: hidden; }
  body { background: var(--backdrop); position: relative; }

  .flyer {
    position: absolute; left: 271px; top: 135px;
    width: 658px; height: 930px;
    background: var(--paper); overflow: hidden;
  }
  .brand { position: absolute; top: 40px; left: 0; width: 100%; text-align: center; }
  .brand-name {
    display: inline-flex; align-items: center; gap: 10px;
    font-family: "Montserrat", sans-serif; font-weight: 700;
    font-size: 52px; letter-spacing: 3px; color: var(--grey); line-height: 1;
  }
  .brand-dot { width: 16px; height: 16px; border-radius: 50%; background: var(--green); }
  .brand-tagline {
    margin-top: 10px;
    font-family: "Montserrat", sans-serif; font-weight: 700;
    font-size: 18px; color: var(--green); letter-spacing: 0.2px;
  }
  .brand-tagline .divider { display: inline-block; width: 1.5px; height: 20px; background: var(--green); margin: 0 12px; vertical-align: -3px; }

  .promo-band { position: absolute; left: 0; top: 143px; width: 100%; height: 369px; background: var(--band); overflow: hidden; }
  .travel-art { position: absolute; background: var(--doodle); border-radius: 8px; }
  .travel-art.plane { left: 58px; top: 8px; width: 112px; height: 40px; }
  .travel-art.camera { left: 534px; top: 93px; width: 80px; height: 58px; }
  .travel-art.suitcase { left: 40px; top: 286px; width: 80px; height: 83px; border-radius: 8px 8px 0 0; }
  .travel-art.glasses { left: 516px; top: 338px; width: 116px; height: 31px; border-radius: 8px 8px 0 0; }

  .headline {
    position: absolute; top: 152px; left: 0; width: 100%; text-align: center;
    font-family: "Londrina Solid", sans-serif; font-weight: 900;
    font-size: 130px; line-height: 111px; letter-spacing: 3px;
  }
  .headline .green { color: var(--green); }
  .headline .grey { color: var(--grey); }

  .offer {
    position: absolute; top: 528px; left: 0; width: 100%; text-align: center;
    font-family: "Bebas Neue", sans-serif; font-size: 52px; line-height: 50px;
    color: var(--grey);
  }
  .offer .hl { color: var(--green); }

  .menu-photo { position: absolute; top: 691px; width: 114px; height: 114px; border-radius: 50%; }
  .menu-photo.bowl { left: 45px; background: radial-gradient(circle, #c98a4f 0%, #e8e4dc 62%, #d8dcdf 100%); }
  .menu-photo.burger { left: 190px; background: radial-gradient(circle, #d59a4c 0%, #c47a3a 45%, #dcdfe1 72%); }
  .menu-photo.plate { left: 344px; background: radial-gradient(circle, #b8773e 0%, #e9e6df 60%, #d7dbde 100%); }
  .menu-photo.cake { left: 498px; background: radial-gradient(circle, #9a6a3e 0%, #e8e2d8 58%, #d7dbde 100%); }

  .deadline {
    position: absolute; left: 153px; top: 825px; width: 357px; height: 45px;
    background: var(--green); border-radius: 11px;
    font-family: "Bebas Neue", sans-serif; font-size: 31px; color: var(--paper);
    display: flex; align-items: center; justify-content: center; padding-top: 2px;
  }
  .website {
    position: absolute; top: 886px; left: 0; width: 100%; text-align: center;
    font-family: "Roboto", sans-serif; font-size: 19px; color: var(--grey); letter-spacing: 0.4px;
  }
</style>
</head>
<body>
  <main class="flyer">
    <header class="brand">
      <div class="brand-name"><span class="brand-dot"></span>VERANDEL</div>
      <div class="brand-tagline">HEALTHY KITCHEN<span class="divider"></span>MEAL PREP</div>
    </header>

    <div class="promo-band">
      <div class="travel-art plane" role="img" aria-label="Line drawing of an airplane"></div>
      <div class="travel-art camera" role="img" aria-label="Line drawing of a camera"></div>
      <div class="travel-art suitcase" role="img" aria-label="Line drawing of a suitcase"></div>
      <div class="travel-art glasses" role="img" aria-label="Line drawing of sunglasses"></div>
    </div>

    <h1 class="headline">
      <span class="green">HOLIDAY</span><br>
      <span class="grey">PACKAGE</span><br>
      <span class="green">PROMO!</span>
    </h1>

    <p class="offer">
      BUY OUR <span class="hl">HOLIDAY PACKAGE</span> OF<br>
      <span class="hl">$500</span> AND RECEIVE A<br>
      <span class="hl">$100</span> GIFT CARD!
    </p>

    <div class="menu-photo bowl" role="img" aria-label="Photo of a loaded rice bowl with drizzled sauce"></div>
    <div class="menu-photo burger" role="img" aria-label="Photo of a chicken burger with lettuce and tomato"></div>
    <div class="menu-photo plate" role="img" aria-label="Photo of grilled fish with greens and sweet potato"></div>
    <div class="menu-photo cake" role="img" aria-label="Photo of a slice of carrot cake"></div>

    <div class="deadline">OFFER ENDS DECEMBER 31ST, 2022</div>
    <p class="website">www.verandelkitchen.com</p>
  </main>
</body>
</html>
```